Infografik im Bereich Artikelbeschreibung für Onlineshop
Zielgruppe
Vertrieb von Saunaaustattung
Aufgabenstellung
Wird als Ergänzung für die Artikelbeschreibung im Webshop benötigt.
Ein Beispiel wo die Infografik platziert werden soll:
https://www.wellforumtech.example/Bilder/beispiel.jpg
Bildgröße ca. 1200 x 800 px
Als Hintergrund eventuell möglich teilweise oder ganz die Grafik mit den blauen Wassertropfen verwendbar?

```html
<!DOCTYPE html>
<html lang="de">
<head>
<meta charset="utf-8">
<title>Dampfgenerator – Ausstattungsmerkmale</title>
<link rel="stylesheet" href="https://fonts.googleapis.com/css2?family=Merriweather:wght@300;400;700&display=swap">
<style>
  :root{
    --bg-top:#dbe9f1;
    --bg-mid:#9cc3da;
    --bg-low:#4f93bb;
    --bg-deep:#2f77a3;
    --ring:#3eb4df;
    --ring-soft:rgba(255,255,255,.55);
    --icon:#3eb4df;
    --label:#15283a;
    --accent:#1c9bd0;
    --white:#ffffff;
    --line:#2a8fbf;
  }
  *{margin:0;padding:0;box-sizing:border-box}
  html,body{width:1200px;height:800px;overflow:hidden}
  body{font-family:"Merriweather",Georgia,serif;color:var(--label)}
  .infographic{position:relative;width:1200px;height:800px;overflow:hidden}
  .backdrop{position:absolute;inset:0}
  .feature-label{
    position:absolute;width:200px;margin-left:-100px;text-align:center;
    font-size:11.5px;line-height:15px;font-weight:700;text-transform:uppercase;letter-spacing:.2px
  }
  .feature-label.light{font-weight:400;color:#1f3447}
  .detail-label{
    position:absolute;width:200px;margin-left:-100px;text-align:center;
    font-size:13px;line-height:17px;font-weight:300;text-transform:uppercase;color:var(--white);letter-spacing:.3px
  }
  .housing-badge{
    position:absolute;left:780px;top:225px;width:190px;height:190px;border-radius:50%;
    background:var(--accent);color:var(--white);display:flex;align-items:center;justify-content:center;
    text-align:center;font-weight:300;font-size:22px;line-height:30px;text-transform:uppercase
  }
</style>
</head>
<body>
<div class="infographic">
  <svg class="backdrop" width="1200" height="800" viewBox="0 0 1200 800">
    <defs>
      <linearGradient id="water" x1="0" y1="0" x2="0.3" y2="1">
        <stop offset="0" stop-color="var(--bg-top)"/>
        <stop offset=".45" stop-color="var(--bg-mid)"/>
        <stop offset=".8" stop-color="var(--bg-low)"/>
        <stop offset="1" stop-color="var(--bg-deep)"/>
      </linearGradient>
      <linearGradient id="steel" x1="0" y1="0" x2="1" y2="1">
        <stop offset="0" stop-color="#eef1f3"/>
        <stop offset=".6" stop-color="#c3c9ce"/>
        <stop offset="1" stop-color="#8e979e"/>
      </linearGradient>
      <radialGradient id="detail" cx=".5" cy=".5" r=".6">
        <stop offset="0" stop-color="#f4f5f6"/>
        <stop offset="1" stop-color="#b9c0c6"/>
      </radialGradient>
    </defs>

    <rect width="1200" height="800" fill="url(#water)" role="img" aria-label="Hintergrund: beschlagene Glasscheibe mit blauen Wassertropfen"/>

    <!-- connector lines -->
    <g stroke="var(--line)" stroke-width="1.5" fill="none">
      <line x1="590" y1="222" x2="1008" y2="170"/>
      <line x1="720" y1="430" x2="1000" y2="405"/>
      <line x1="742" y1="510" x2="1006" y2="600"/>
    </g>

    <!-- product -->
    <polygon points="418,210 470,195 762,215 762,545 700,562 418,520" fill="url(#steel)" role="img" aria-label="Produktfoto: Dampfgenerator im Edelstahlgehäuse mit Anschlüssen"/>

    <!-- detail photos -->
    <g stroke="var(--ring)" stroke-width="3">
      <circle cx="1063" cy="172" r="58" fill="url(#detail)" role="img" aria-label="Detailfoto: Entkalkungsverschluss"/>
      <circle cx="1065" cy="385" r="66" fill="url(#detail)" role="img" aria-label="Detailfoto: Heizstab"/>
      <circle cx="1063" cy="592" r="60" fill="url(#detail)" role="img" aria-label="Detailfoto: Abflussventil"/>
    </g>

    <!-- icon discs -->
    <g fill="var(--white)" stroke="var(--ring)" stroke-width="3">
      <circle cx="130" cy="87" r="48"/><circle cx="130" cy="240" r="48"/>
      <circle cx="130" cy="380" r="48"/><circle cx="130" cy="516" r="48"/>
      <circle cx="130" cy="652" r="48"/>
      <circle cx="357" cy="83" r="48"/><circle cx="525" cy="83" r="48"/>
      <circle cx="695" cy="83" r="48"/><circle cx="857" cy="83" r="48"/>
      <circle cx="305" cy="655" r="48"/><circle cx="477" cy="655" r="48"/>
      <circle cx="633" cy="655" r="48"/><circle cx="793" cy="655" r="48"/>
    </g>

    <g fill="none" stroke="var(--icon)" stroke-width="2.5" stroke-linecap="round" stroke-linejoin="round">
      <!-- aroma nozzle -->
      <circle cx="130" cy="88" r="14" fill="var(--icon)"/>
      <line x1="110" y1="110" x2="104" y2="118"/><line x1="130" y1="112" x2="130" y2="122"/><line x1="150" y1="110" x2="156" y2="118"/>
      <!-- clock -->
      <path d="M106 240 a24 24 0 1 0 8 -18"/><path d="M108 218 l6 4 -6 5"/>
      <!-- A flasks B -->
      <circle cx="120" cy="384" r="8" fill="var(--icon)"/><circle cx="140" cy="384" r="8" fill="var(--icon)"/>
      <!-- phone -->
      <rect x="115" y="492" width="28" height="44" rx="4"/><path d="M132 520 v14 l8 8 h8 l2 -12 -10 -4"/>
      <!-- descaling arrow -->
      <path d="M118 640 h24 v12 h10 l-22 20 -22 -20 h10 z"/><circle cx="128" cy="630" r="3"/><circle cx="140" cy="626" r="3"/>
      <!-- shield thermometer -->
      <path d="M357 58 l22 8 v16 c0 14 -10 22 -22 28 c-12 -6 -22 -14 -22 -28 v-16 z"/>
      <path d="M357 70 v22"/><circle cx="357" cy="94" r="4" fill="var(--icon)"/>
      <!-- broom -->
      <path d="M542 60 l-14 22"/><path d="M520 78 l16 10 c-4 10 -14 16 -26 16 c4 -10 4 -18 10 -26 z" fill="var(--icon)"/>
      <!-- compact size -->
      <path d="M675 66 v34 h40"/><path d="M675 66 h40 v10" stroke-dasharray="4 3"/>
      <!-- virus crossed -->
      <circle cx="857" cy="83" r="26"/><line x1="838" y1="64" x2="876" y2="102"/><circle cx="857" cy="83" r="10" fill="var(--icon)"/>
      <!-- bulb -->
      <path d="M293 668 c0 -10 -12 -14 -12 -28 a24 24 0 0 1 48 0 c0 14 -12 18 -12 28 z"/><line x1="295" y1="676" x2="317" y2="676"/><line x1="298" y1="684" x2="314" y2="684"/>
      <!-- salt -->
      <rect x="470" y="628" width="22" height="34" rx="3" transform="rotate(35 481 645)" fill="var(--icon)"/><circle cx="462" cy="670" r="2"/><circle cx="468" cy="678" r="2"/>
      <!-- thermometer -->
      <path d="M629 630 v34 a10 10 0 1 0 8 0 v-34 a4 4 0 0 0 -8 0 z"/><circle cx="633" cy="672" r="5" fill="var(--icon)"/>
      <!-- fan -->
      <circle cx="793" cy="655" r="5"/><path d="M793 650 c-4 -14 10 -20 14 -10 z M798 657 c12 4 8 18 -2 14 z M788 657 c-10 8 -20 -4 -10 -10 z"/>
    </g>
    <text x="130" y="243" font-family="Merriweather,serif" font-size="9" fill="var(--icon)" text-anchor="middle">4 - 8</text>
    <text x="130" y="255" font-family="Merriweather,serif" font-size="9" fill="var(--icon)" text-anchor="middle">min</text>
    <text x="104" y="388" font-family="Merriweather,serif" font-size="12" font-weight="700" fill="var(--icon)" text-anchor="middle">A</text>
    <text x="156" y="388" font-family="Merriweather,serif" font-size="12" font-weight="700" fill="var(--icon)" text-anchor="middle">B</text>
    <text x="697" y="90" font-family="Merriweather,serif" font-size="12" fill="var(--icon)" text-anchor="middle">cm²</text>
  </svg>

  <div class="feature-label" style="left:130px;top:149px">Inkludierte<br>Armoaauslassdüse</div>
  <div class="feature-label" style="left:130px;top:298px">Kurze Aufheizzeit</div>
  <div class="feature-label" style="left:130px;top:439px">Ansteuerung von bis<br>zu zwei Duftstoffen</div>
  <div class="feature-label light" style="left:130px;top:574px">Optional<br>Steuerung per App</div>
  <div class="feature-label light" style="left:130px;top:730px">Elektronische<br>Entkalkung</div>

  <div class="feature-label" style="left:357px;top:158px">Thermoschutz</div>
  <div class="feature-label" style="left:525px;top:151px">Automatische<br>Selbstreinigung</div>
  <div class="feature-label" style="left:695px;top:149px">Kompakte<br>Größe</div>
  <div class="feature-label" style="left:857px;top:151px">Gerät kocht auf<br>ca. 100 C° hoch</div>

  <div class="feature-label light" style="left:305px;top:730px">Farblichtsteuerung</div>
  <div class="feature-label light" style="left:477px;top:730px">Ansteuerung<br>Salzsolevernebler</div>
  <div class="feature-label light" style="left:633px;top:732px">Verbrühschutz<br>Abfluss</div>
  <div class="feature-label light" style="left:793px;top:730px">Integrierte<br>Abluftsteuerung</div>
  <div class="feature-label light" style="left:930px;top:727px">Steuerdisplay<br>fliesenbündig<br>einbaubar</div>

  <div class="detail-label" style="left:1063px;top:249px">Manuelles<br>Entkalken</div>
  <div class="detail-label" style="left:1065px;top:469px">Hochleistungs-<br>heizstäbe</div>
  <div class="detail-label" style="left:1063px;top:690px">Elektronisches<br>Abflussventil</div>

  <div class="housing-badge">Gehäuse<br>Edelstahl<br>S304</div>
</div>
</body>
</html>
```